Letterhead Design Needed for Real Estate Office

We are a boutique real estate agency focused on property management. We need a letter head which is professional looking and include the following information:

Logo
ABN Number
Address
Postal Address
Phone
Fax
Mobile
Email
Website

Please note that the PLBVKT logo can not be changed and must be positioned at the bottom right corner.

Please find attached the existing letterhead design for all the required elements.

Target Market(s)

Letterhead mostly used for service of notices, business letters, clients communication

Industry/Entity Type

Boutique

Colors

Designer to choose colors to be used in the design.

Requirements
Must have
• Logo

```html
<!DOCTYPE html>
<html lang="en">
<head>
<meta charset="utf-8">
<title>Halcyon Partners Letterhead</title>
<link rel="stylesheet" href="https://fonts.googleapis.com/css2?family=Source+Sans+3:wght@400;600;700&display=swap">
<style>
  :root {
    --paper: #ffffff;
    --ink: #1a1a1a;
    --brand-green: #7ab648;
    --brand-dark: #111111;
    --member-blue: #1f5d99;
    --on-dark: #ffffff;
  }
  * { margin: 0; padding: 0; box-sizing: border-box; }
  html, body { width: 1022px; height: 1200px; overflow: hidden; background: var(--paper); }
  body { font-family: "Source Sans 3", Arial, sans-serif; color: var(--ink); }

  .letterhead { position: relative; width: 1022px; height: 1200px; background: var(--paper); }

  .brand { position: absolute; top: 62px; left: 0; width: 100%; display: flex; justify-content: center; align-items: center; gap: 18px; }
  .brand-square { width: 58px; height: 58px; background: var(--brand-green); }
  .brand-name { font-size: 44px; font-weight: 700; letter-spacing: 1px; color: var(--ink); line-height: 1; }

  .member { position: absolute; right: 50px; top: 1060px; display: flex; align-items: center; gap: 12px; }
  .member-circle { width: 34px; height: 34px; border-radius: 50%; background: var(--member-blue); }
  .member-name { font-size: 40px; font-weight: 600; color: var(--member-blue); line-height: 1; }

  .address-band { position: absolute; left: 0; top: 1121px; width: 100%; height: 28px; background: var(--brand-green); color: var(--on-dark); font-size: 15px; display: flex; align-items: center; justify-content: center; }

  .contact-band { position: absolute; left: 0; top: 1151px; width: 100%; height: 49px; background: var(--brand-dark); color: var(--on-dark); font-size: 15px; display: flex; align-items: center; justify-content: center; gap: 14px; }
  .contact-item { display: flex; align-items: center; gap: 6px; }
  .contact-item svg { width: 13px; height: 13px; fill: var(--on-dark); }
</style>
</head>
<body>
<div class="letterhead">
  <header class="brand">
    <div class="brand-square"></div>
    <div class="brand-name">HALCYON PARTNERS</div>
  </header>

  <div class="member">
    <div class="member-circle"></div>
    <div class="member-name">PLBVKT</div>
  </div>

  <div class="address-band">Shop 12B 218-230 Harbour Street Lindfield NSW 2070 AUSTRALIA | PO BOX 415 Lindfield NSW 2070 | ABN: 48 302 517 694</div>

  <footer class="contact-band">
    <span class="contact-item">
      <svg viewBox="0 0 16 16"><path d="M3 1l3 3-1.5 2a9 9 0 0 0 5.5 5.5L12 10l3 3-2 2C6 15 1 10 1 3z"/></svg>9380 1726
    </span>
    <span class="contact-item">
      <svg viewBox="0 0 16 16"><path d="M4 0h8v16H4zM5.5 2v9h5V2zM7 13h2v1.5H7z" fill-rule="evenodd"/></svg>0412 553 907
    </span>
    <span class="contact-item">
      <svg viewBox="0 0 16 16"><path d="M4 1h7v4H4zM1 6h14v7h-3v2H4v-2H1zM5 10v4h6v-4z" fill-rule="evenodd"/></svg>9380 1730
    </span>
    <span class="contact-item">
      <svg viewBox="0 0 16 16"><path d="M1 3h14v1L8 9 1 4zM1 6l7 5 7-5v7H1z"/></svg>hello@halcyonre.cc
    </span>
    <span class="contact-item">
      <svg viewBox="0 0 16 16"><path d="M8 1a7 7 0 1 0 0 14A7 7 0 0 0 8 1zm0 1.5c1 1.2 1.6 3 1.7 4.8H6.3C6.4 5.5 7 3.7 8 2.5zM2.6 8.7h2.3c.1 1.7.5 3.3 1.2 4.5a5.6 5.6 0 0 1-3.5-4.5zm0-1.4a5.6 5.6 0 0 1 3.5-4.5c-.7 1.2-1.1 2.8-1.2 4.5zM8 13.5c-1-1.2-1.6-3-1.7-4.8h3.4c-.1 1.8-.7 3.6-1.7 4.8zm1.9-.3c.7-1.2 1.1-2.8 1.2-4.5h2.3a5.6 5.6 0 0 1-3.5 4.5zm1.2-5.9c-.1-1.7-.5-3.3-1.2-4.5a5.6 5.6 0 0 1 3.5 4.5z"/></svg>www.halcyonre.cc
    </span>
  </footer>
</div>
</body>
</html>
```